Medical Oncologist in Rural Australia needs a Business Card

I am a medical oncologist in a regional town in Australia. I need a business card that merges a degree of conservatism (as people's lives are entrusted to me) with cutting edge (as I am always trying to understand the latest cancer biology and trying to bring new drugs to patients rapidly). I wish my card to project the idea that I am trustworthy, caring and innovative. Not overly bold colours but something that doesn't drift into the background.

Medical

```html
<!DOCTYPE html>
<html lang="en">
<head>
<meta charset="utf-8">
<title>Medical Oncologist – Business Card</title>
<link rel="stylesheet" href="https://fonts.googleapis.com/css2?family=Exo+2:wght@400;600;700;800&family=Dancing+Script:wght@700&display=swap">
<style>
  :root {
    --backdrop: #e4e4e6;
    --card-light: #f3f3f4;
    --card-mid: #dcdcde;
    --blue-deep: #3f62a8;
    --blue-soft: #6b8cc8;
    --blue-text: #5479bd;
    --ink: #1d1d1f;
    --silver: #eeeeee;
  }
  * { box-sizing: border-box; margin: 0; padding: 0; }
  html, body { width: 1200px; height: 750px; overflow: hidden; }
  body {
    background: var(--backdrop);
    font-family: "Exo 2", sans-serif;
    position: relative;
  }
  .card {
    position: absolute;
    width: 520px;
    height: 300px;
    border-radius: 26px;
    overflow: hidden;
    background: linear-gradient(160deg, var(--card-light), var(--card-mid));
    box-shadow: 0 6px 18px rgba(0,0,0,0.18);
  }
  .card-front { left: 70px; top: 80px; }
  .card-back { left: 610px; top: 370px; }

  .wave { position: absolute; inset: 0; width: 100%; height: 100%; }

  .front-title {
    position: absolute;
    left: 120px;
    top: 95px;
    line-height: 0.9;
    font-weight: 800;
    letter-spacing: 1px;
  }
  .front-title .word-medical { display: block; font-size: 46px; color: var(--ink); }
  .front-title .word-oncologist {
    display: block; font-size: 54px; color: var(--silver);
    text-shadow: 2px 2px 0 rgba(20,20,30,0.85);
  }
  .front-quote {
    position: absolute;
    left: 150px;
    top: 210px;
    font-family: "Dancing Script", cursive;
    font-size: 30px;
    color: var(--ink);
  }

  .back-title {
    position: absolute;
    left: 34px;
    top: 70px;
    line-height: 0.9;
    font-weight: 800;
    letter-spacing: 1px;
  }
  .back-title .word-medical { display: block; font-size: 34px; color: var(--ink); }
  .back-title .word-oncologist { display: block; font-size: 40px; color: var(--blue-text); }

  .doctor {
    position: absolute;
    left: 250px;
    top: 58px;
    white-space: nowrap;
  }
  .doctor .prefix {
    font-family: "Dancing Script", cursive;
    font-size: 30px;
    color: var(--blue-text);
  }
  .doctor .name { font-size: 42px; font-weight: 700; color: var(--ink); }
  .credentials {
    position: absolute;
    left: 262px;
    top: 112px;
    font-size: 11.5px;
    font-weight: 600;
    color: var(--ink);
    white-space: nowrap;
  }

  .contact-list {
    position: absolute;
    left: 34px;
    top: 170px;
    list-style: none;
  }
  .contact-list li {
    display: flex;
    align-items: center;
    gap: 12px;
    height: 34px;
    font-size: 24px;
    color: var(--blue-text);
    font-weight: 400;
    letter-spacing: 0.5px;
  }
  .contact-list svg { width: 22px; height: 22px; fill: #555; flex: none; }
</style>
</head>
<body>

<section class="card card-front" aria-label="Card front">
  <svg class="wave" viewBox="0 0 520 300" preserveAspectRatio="none" aria-hidden="true">
    <defs>
      <linearGradient id="bandBlue" x1="0" y1="1" x2="1" y2="0">
        <stop offset="0" stop-color="var(--blue-soft)"/>
        <stop offset="1" stop-color="var(--blue-deep)"/>
      </linearGradient>
    </defs>
    <path d="M0 95 C 110 40, 250 5, 520 25 L520 300 L0 300 Z" fill="url(#bandBlue)"/>
  </svg>
  <h1 class="front-title">
    <span class="word-medical">medical</span>
    <span class="word-oncologist">oncologist</span>
  </h1>
  <p class="front-quote">your quote here</p>
</section>

<section class="card card-back" aria-label="Card back">
  <h2 class="back-title">
    <span class="word-medical">medical</span>
    <span class="word-oncologist">oncologist</span>
  </h2>
  <p class="doctor"><span class="prefix">dr.</span> <span class="name">Your Name</span></p>
  <p class="credentials">specialized in MBBS (hons), FRACP, BE (hons)</p>
  <ul class="contact-list">
    <li>
      <svg viewBox="0 0 24 24" aria-hidden="true"><path d="M7 1h10a2 2 0 0 1 2 2v18a2 2 0 0 1-2 2H7a2 2 0 0 1-2-2V3a2 2 0 0 1 2-2zm0 3v14h10V4zm5 15.5a1.2 1.2 0 1 0 0 2.4 1.2 1.2 0 0 0 0-2.4z"/></svg>
      0 123 456 89
    </li>
    <li>
      <svg viewBox="0 0 24 24" aria-hidden="true"><path d="M3 9c0-3 4-5 9-5s9 2 9 5v2h-5V9H8v2H3zm3 4h12l2 8H4zm6 1.5a3 3 0 1 0 0 6 3 3 0 0 0 0-6z"/></svg>
      0 123 456 78
    </li>
    <li>
      <svg viewBox="0 0 24 24" aria-hidden="true"><path d="M12 2a10 10 0 1 0 5 18.7l-1-1.7A8 8 0 1 1 20 12v1.2a1.8 1.8 0 0 1-3.6 0V7h-2v1a5 5 0 1 0 .6 7.4 3.8 3.8 0 0 0 7-2.2V12A10 10 0 0 0 12 2zm0 13a3 3 0 1 1 0-6 3 3 0 0 1 0 6z"/></svg>
      yourname@example.com
    </li>
  </ul>
</section>

</body>
</html>
```